Unique Mendrix Building Bussiness Card Design

www.mendrix.com.au

Please see website for Company profile. We require a design that incorporates our logo colours and is unique in shape and style compared to all other business cards.

www.mendrix.com.au

INSPIRE US !!!
Updates

Target Market(s)

Facility managers, Building Managers, Architects

Industry/Entity Type

Business

Contact Information for Business Card

Mendrix Building Solutions
Project Manager
Dennis Harwood
0437 619 204
Sales@mendrix.com.au

Logo Text

Mendrix Building Solutions

Logo styles of interest
Abstract Logo
Requirements
Nice to have
• Card must show we are an established big business to trust.

```html
<!DOCTYPE html>
<html lang="en">
<head>
<meta charset="utf-8">
<title>Mendrix Building Solutions – Business Card</title>
<link rel="stylesheet" href="https://fonts.googleapis.com/css2?family=Ubuntu:wght@400;700&family=Alegreya+Sans+SC:wght@500;700&display=swap">
<style>
  :root {
    --stage: #ecebe8;
    --orange: #ea6a2c;
    --orange-light: #f28c3c;
    --orange-deep: #d9531f;
    --brick: #b8281f;
    --brick-dark: #8f1d17;
    --navy: #1e4f80;
    --ink: #1c1c1c;
    --paper: #ffffff;
    --white: #ffffff;
  }
  * { margin: 0; padding: 0; box-sizing: border-box; }
  html, body { width: 1200px; height: 785px; overflow: hidden; }
  body {
    background: var(--stage);
    font-family: "Ubuntu", sans-serif;
    position: relative;
  }
  .card {
    position: absolute;
    top: 235px;
    width: 550px;
    height: 315px;
    overflow: hidden;
    box-shadow: 0 6px 18px rgba(0,0,0,0.18);
  }

  /* ---------- Back of card ---------- */
  .card-back {
    left: 35px;
    background: linear-gradient(160deg, var(--orange-light) 0%, var(--orange) 55%, var(--orange-deep) 100%);
  }
  .card-back .facets { position: absolute; inset: 0; }
  .services {
    position: absolute;
    top: 22px;
    left: 300px;
    list-style: none;
    color: var(--white);
    font-size: 14px;
    line-height: 17px;
  }
  .services li::before { content: "•"; margin-right: 7px; font-size: 10px; vertical-align: 2px; }
  .services li:nth-child(2) { padding-left: 6px; }
  .services li:nth-child(3) { padding-left: 12px; }
  .services li:nth-child(4) { padding-left: 18px; }
  .services li:nth-child(5) { padding-left: 24px; }
  .services li:nth-child(6) { padding-left: 30px; }
  .back-brand {
    position: absolute;
    left: 230px;
    top: 190px;
    color: var(--white);
  }
  .back-brand .brand-name {
    font-size: 42px;
    font-weight: 700;
    letter-spacing: 0.5px;
    line-height: 1;
  }
  .back-brand .tagline {
    margin-top: 6px;
    font-size: 13px;
    letter-spacing: 1px;
  }

  /* ---------- Front of card ---------- */
  .card-front {
    left: 615px;
    background: var(--paper);
  }
  .contact-person {
    position: absolute;
    top: 26px;
    right: 24px;
    text-align: right;
    font-family: "Alegreya Sans SC", sans-serif;
  }
  .contact-person .person-name {
    color: var(--navy);
    font-size: 19px;
    font-weight: 700;
    letter-spacing: 0.5px;
  }
  .contact-person .person-role {
    color: var(--brick);
    font-size: 13px;
    font-weight: 500;
  }
  .front-brand {
    position: absolute;
    top: 110px;
    left: 22px;
    display: flex;
    align-items: center;
    gap: 10px;
  }
  .front-brand .brand-mark {
    width: 22px;
    height: 22px;
    background: var(--orange);
  }
  .front-brand .brand-name {
    color: var(--navy);
    font-size: 34px;
    font-weight: 700;
    line-height: 1;
  }
  .front-brand-tagline {
    position: absolute;
    top: 150px;
    left: 56px;
    color: var(--brick);
    font-size: 12px;
    letter-spacing: 1px;
  }
  .handshake-art {
    position: absolute;
    top: 95px;
    right: 22px;
    width: 180px;
    height: 100px;
    border-radius: 40px;
    background: linear-gradient(90deg, #c9463e 0%, #8a6a8f 50%, #2f5c93 100%);
    opacity: 0.85;
  }
  .contact-list {
    position: absolute;
    left: 26px;
    top: 200px;
    list-style: none;
    color: var(--ink);
    font-size: 17px;
    line-height: 24px;
  }
  .contact-list li { display: flex; align-items: center; gap: 8px; }
  .contact-list svg { width: 18px; height: 18px; flex: none; }
  .contact-list .phone { font-size: 20px; letter-spacing: 1.5px; }
  .front-band {
    position: absolute;
    left: 0; right: 0; bottom: 0;
    height: 22px;
    background: linear-gradient(90deg, var(--orange-deep), var(--orange-light));
  }
</style>
</head>
<body>

  <section class="card card-back" aria-label="Business card back">
    <svg class="facets" viewBox="0 0 550 315" preserveAspectRatio="none" aria-hidden="true">
      <polygon points="0,0 210,0 150,315 0,315" fill="#e0592a" opacity="0.6"/>
      <polygon points="40,110 180,70 230,315 70,315" fill="var(--brick)"/>
      <polygon points="70,160 160,140 200,315 100,315" fill="var(--brick-dark)" opacity="0.7"/>
      <polygon points="210,0 330,0 250,160" fill="#f5a066" opacity="0.35"/>
    </svg>
    <ul class="services">
      <li>Project Management</li>
      <li>Building</li>
      <li>Shopfitting</li>
      <li>Residential</li>
      <li>Commercial</li>
      <li>Joinery</li>
    </ul>
    <div class="back-brand">
      <div class="brand-name">Mendrix.com.au</div>
      <div class="tagline">Construction Excellence</div>
    </div>
  </section>

  <section class="card card-front" aria-label="Business card front">
    <div class="contact-person">
      <div class="person-name">Dennis Harwood</div>
      <div class="person-role">Project Manager</div>
    </div>

    <div class="front-brand">
      <span class="brand-mark"></span>
      <span class="brand-name">Mendrix.com.au</span>
    </div>
    <div class="front-brand-tagline">Construction Excellence</div>

    <div class="handshake-art" role="img" aria-label="Illustration of two hands shaking, drawn in red and blue line strokes"></div>

    <ul class="contact-list">
      <li class="phone">
        <svg viewBox="0 0 20 20" aria-hidden="true"><path d="M3 6 Q3 3 6 3 L14 3 Q17 3 17 6 L17 8 L13 8 L13 6 L7 6 L7 8 L3 8 Z M5 9 L15 9 L17 17 L3 17 Z" fill="var(--navy)"/><circle cx="10" cy="13" r="2" fill="var(--paper)"/></svg>
        0437 619 204
      </li>
      <li>
        <svg viewBox="0 0 20 20" aria-hidden="true"><rect x="2" y="4" width="16" height="12" fill="none" stroke="var(--navy)" stroke-width="1.5"/><polyline points="2,4 10,11 18,4" fill="none" stroke="var(--navy)" stroke-width="1.5"/></svg>
        Sales@mendrix.com.au
      </li>
      <li>
        <svg viewBox="0 0 20 20" aria-hidden="true"><circle cx="10" cy="10" r="8" fill="var(--navy)"/><g fill="none" stroke="var(--paper)" stroke-width="1"><ellipse cx="10" cy="10" rx="3.5" ry="8"/><line x1="2" y1="10" x2="18" y2="10"/><line x1="3.5" y1="6" x2="16.5" y2="6"/><line x1="3.5" y1="14" x2="16.5" y2="14"/></g></svg>
        www.mendrix.com.au
      </li>
    </ul>

    <div class="front-band"></div>
  </section>

</body>
</html>
```